Freelancer Information Security professional needs a business card

I need a simple, young, elegant business card. I'm a freelancer in the InfoSec area and want to be able to give my card to potential customers and new people I meet.

I'd like to have a clean, professional look but at same time not boring or corporate.

The only requirement is to have my "introduction" phrase which is:
"Half hacker, half mercenary."

I have added a card I have as a example, which I think it gives a good example of style I want.

Target Market(s)

Technology / Computers / Engineering

Industry/Entity Type

Information Technology

Contact Information for Business Card

Contact fields I want included:

(351) 93 708 12 54
tomas@vornel.im
https://vornel.im

Font styles to use
Sans Serif

Requirements
Nice to have
• Card doesn't need to have a doubled side, but it looks good / fits the design then please do include.
Should not have
• Outdated graphics or images; too much patterns/colors.

```html
<!DOCTYPE html>
<html lang="en">
<head>
<meta charset="utf-8">
<title>Tomas Vornel — Business Card</title>
<link href="https://fonts.googleapis.com/css2?family=Open+Sans:wght@700;800&family=Abel&display=swap" rel="stylesheet">
<style>
  :root {
    --page-bg: #ffffff;
    --navy: #2f3586;
    --blue-top: #343a88;
    --blue-bottom: #2873bb;
    --gold: #d9b15f;
    --gold-light: #f3e5c2;
    --silver-edge: #c9cbcc;
    --silver-mid: #eceeee;
    --silver-light: #ffffff;
    --ink: #2a2a2a;
    --icon: #2f3586;
    --white: #ffffff;
    --mark-ink: #222222;
  }
  html, body {
    margin: 0;
    padding: 0;
    width: 950px;
    height: 1200px;
    overflow: hidden;
    background: var(--page-bg);
  }
  .canvas {
    position: relative;
    width: 950px;
    height: 1200px;
  }
  .card {
    position: absolute;
    width: 771px;
    height: 452px;
    background: linear-gradient(90deg,
      var(--silver-edge) 0%,
      var(--silver-mid) 18%,
      #fafafa 38%,
      var(--silver-light) 62%,
      #f3f4f4 78%,
      var(--silver-edge) 94%,
      #d3d5d5 100%);
    box-shadow: 10px 12px 10px rgba(0, 0, 0, 0.28);
    overflow: hidden;
  }
  .card--front { left: 96px; top: 61px; }
  .card--back  { left: 93px; top: 650px; }

  .card__header {
    position: absolute;
    left: 0;
    top: 0;
    width: 771px;
    height: 240px;
  }
  .card__name {
    position: absolute;
    top: 64px;
    left: 0;
    width: 100%;
    margin: 0;
    text-align: center;
    font-family: "Open Sans", Arial, sans-serif;
    font-weight: 700;
    font-size: 26px;
    letter-spacing: 0.3px;
    color: var(--white);
  }
  .card__tagline {
    position: absolute;
    top: 133px;
    left: 0;
    width: 100%;
    margin: 0;
    text-align: center;
    font-family: "Open Sans", Arial, sans-serif;
    font-weight: 700;
    font-size: 18px;
    letter-spacing: 0.3px;
    color: var(--white);
  }
  .contact-list {
    position: absolute;
    left: 260px;
    top: 266px;
    margin: 0;
    padding: 0;
    list-style: none;
  }
  .contact-list__item {
    display: flex;
    align-items: center;
    height: 47px;
    font-family: "Abel", "Arial Narrow", sans-serif;
    font-size: 28px;
    letter-spacing: 0.5px;
    color: var(--ink);
  }
  .contact-list__icon {
    width: 22px;
    height: 22px;
    margin-right: 16px;
    flex: none;
  }
  .brand-mark {
    position: absolute;
    left: 0;
    top: 200px;
    width: 100%;
    margin: 0;
    text-align: center;
    font-family: "Open Sans", Arial, sans-serif;
    font-weight: 700;
    font-size: 26px;
    letter-spacing: 0.3px;
    color: var(--mark-ink);
  }
</style>
</head>
<body>
<main class="canvas">

  <section class="card card--front">
    <svg class="card__header" viewBox="0 0 771 240" aria-hidden="true">
      <defs>
        <linearGradient id="headerBlue" x1="0" y1="0" x2="0" y2="1">
          <stop offset="0" stop-color="var(--blue-top)"/>
          <stop offset="0.55" stop-color="#2b5fac"/>
          <stop offset="1" stop-color="var(--blue-bottom)"/>
        </linearGradient>
        <linearGradient id="goldBand" x1="0" y1="0" x2="1" y2="0">
          <stop offset="0" stop-color="#c9a25a"/>
          <stop offset="0.25" stop-color="var(--gold-light)"/>
          <stop offset="0.5" stop-color="var(--gold)"/>
          <stop offset="0.75" stop-color="var(--gold-light)"/>
          <stop offset="1" stop-color="#c9a25a"/>
        </linearGradient>
      </defs>
      <path d="M0 0 H771 V184 Q385.5 248 0 184 Z" fill="url(#goldBand)"/>
      <path d="M0 0 H771 V175 Q385.5 237 0 175 Z" fill="url(#headerBlue)"/>
      <path d="M0 188 Q385.5 252 771 188" fill="none" stroke="var(--navy)" stroke-width="3"/>
    </svg>

    <h1 class="card__name">TOMAS VORNEL</h1>
    <p class="card__tagline">HALF HACKER, HALF MERCENARY.</p>

    <ul class="contact-list">
      <li class="contact-list__item">
        <svg class="contact-list__icon" viewBox="0 0 22 22" aria-hidden="true">
          <rect x="5" y="2" width="12" height="18" rx="2" fill="none" stroke="var(--icon)" stroke-width="1.6"/>
          <line x1="9" y1="17" x2="13" y2="17" stroke="var(--icon)" stroke-width="1.4"/>
        </svg>
        (351) 93 708 12 54
      </li>
      <li class="contact-list__item">
        <svg class="contact-list__icon" viewBox="0 0 22 22" aria-hidden="true">
          <rect x="2" y="5" width="18" height="12" fill="none" stroke="var(--icon)" stroke-width="1.5"/>
          <path d="M2 5 L11 12 L20 5 M2 17 L9 10.5 M20 17 L13 10.5" fill="none" stroke="var(--icon)" stroke-width="1.3"/>
        </svg>
        tomas@vornel.im
      </li>
      <li class="contact-list__item">
        <svg class="contact-list__icon" viewBox="0 0 22 22" aria-hidden="true">
          <circle cx="11" cy="11" r="9" fill="none" stroke="var(--icon)" stroke-width="1.5"/>
          <ellipse cx="11" cy="11" rx="4" ry="9" fill="none" stroke="var(--icon)" stroke-width="1.3"/>
          <line x1="2" y1="11" x2="20" y2="11" stroke="var(--icon)" stroke-width="1.3"/>
          <line x1="11" y1="2" x2="11" y2="20" stroke="var(--icon)" stroke-width="1.3"/>
        </svg>
        https://vornel.im
      </li>
    </ul>
  </section>

  <section class="card card--back">
    <p class="brand-mark">TOMAS VORNEL</p>
  </section>

</main>
</body>
</html>
```